TKA Electricial Contracting Services

Hi guys, after a design for my small electrical company, have logo design files to be incorporated into the layout, the basic concept is electrical contracting services for residential, commercial, industrial & data services, image is clean clear and strong,

Card format is to have a nice clean logo on front,with maybe the Residential – commercial – industrial - data, followed with licensed & insured, followed by contact details on backside of the card.

Target Market(s)

Residential, commercial, industrial sectors.

Industry/Entity Type

Electrical

Contact Information for Business Card

TKA logo,
Residential – commercial – industrial - data
REC: 61372
Email: tka@poralink.net.au
Phone: 0458 203 719

Requirements
Must have
• Clean & strong design.
Nice to have
• If possible, I would like the logo colours inverted so the text is orange and the background is black on the front of the card, then the backside of the card be the reverse colour
Should not have
• No Sparks, lightning bolts,

```html
<!DOCTYPE html>
<html lang="en">
<head>
<meta charset="utf-8">
<title>TKA Electrical Contracting Services – Business Card</title>
<link rel="stylesheet" href="https://fonts.googleapis.com/css2?family=Exo+2:wght@500;600;700;800&display=swap">
<style>
  :root {
    --stage: #2f3d43;
    --card-black: #050505;
    --card-charcoal: #1e1c21;
    --orange: #f07f22;
    --white: #f4f4f4;
  }
  * { margin: 0; padding: 0; box-sizing: border-box; }
  html, body { width: 1200px; height: 900px; overflow: hidden; }
  body {
    background: var(--stage);
    font-family: "Exo 2", sans-serif;
    position: relative;
  }
  .card {
    position: absolute;
    left: 320px;
    width: 560px;
    height: 320px;
    border-radius: 16px;
    overflow: hidden;
    border-top: 16px solid var(--orange);
    border-bottom: 16px solid var(--orange);
  }
  .card--contact { top: 70px; background: var(--card-black); }
  .card--logo { top: 500px; background: var(--card-charcoal); }

  /* Contact side */
  .brand-block {
    position: absolute;
    top: 14px;
    right: 34px;
    text-align: right;
  }
  .brand-mark {
    display: block;
    font-size: 60px;
    font-weight: 800;
    line-height: 1;
    letter-spacing: 1px;
    color: var(--white);
  }
  .brand-name {
    display: block;
    margin-top: 4px;
    font-size: 16px;
    font-weight: 700;
    color: var(--orange);
  }
  .services {
    font-size: 14px;
    font-weight: 600;
    line-height: 1.25;
    color: var(--orange);
  }
  .person {
    position: absolute;
    left: 26px;
    top: 146px;
  }
  .person-name {
    font-size: 21px;
    font-weight: 700;
    color: var(--orange);
  }
  .person-role {
    font-size: 13px;
    font-weight: 600;
    color: var(--white);
  }
  .contact-list {
    list-style: none;
    position: absolute;
    left: 22px;
    top: 210px;
    font-size: 16px;
    font-weight: 600;
    color: var(--orange);
  }
  .contact-list li { display: flex; align-items: center; gap: 8px; height: 22px; }
  .contact-list svg { width: 14px; height: 14px; }

  /* Logo side */
  .logo-lockup {
    position: absolute;
    inset: 0;
    display: flex;
    flex-direction: column;
    align-items: center;
    justify-content: center;
  }
  .logo-mark {
    font-size: 130px;
    font-weight: 800;
    line-height: 0.9;
    letter-spacing: 2px;
    color: var(--white);
  }
  .logo-name {
    margin-top: 8px;
    font-size: 32px;
    font-weight: 600;
    color: var(--white);
  }
</style>
</head>
<body>
  <section class="card card--contact" aria-label="Business card contact side">
    <div class="brand-block">
      <span class="brand-mark">TKA</span>
      <span class="brand-name">Tate Kirby Electrical</span>
      <p class="services">licenced &amp; insured Residential<br>commercial – industrial – data REC: 61372</p>
    </div>
    <div class="person">
      <p class="person-name">Alex Carter</p>
      <p class="person-role">Owner</p>
    </div>
    <ul class="contact-list">
      <li>
        <svg viewBox="0 0 14 14" aria-hidden="true"><path d="M3 1.5 L5 1.5 L6 4.5 L4.6 5.6 Q5.8 8.2 8.4 9.4 L9.5 8 L12.5 9 L12.5 11 Q12 12.8 10 12.5 Q2 11 1.5 4 Q1.3 2 3 1.5Z" fill="none" stroke="#f4f4f4" stroke-width="1.3"/></svg>
        0458 203 719
      </li>
      <li>
        <svg viewBox="0 0 14 14" aria-hidden="true"><rect x="1" y="3" width="12" height="8" fill="none" stroke="#f4f4f4" stroke-width="1.2"/><path d="M1 3 L7 8 L13 3" fill="none" stroke="#f4f4f4" stroke-width="1.2"/></svg>
        tka@poralink.net.au
      </li>
    </ul>
  </section>

  <section class="card card--logo" aria-label="Business card logo side">
    <div class="logo-lockup">
      <span class="logo-mark">TKA</span>
      <span class="logo-name">Tate Kirby Electrical</span>
    </div>
  </section>
</body>
</html>
```